Atelier Vireo Crandt Coming Soon

Launching a online mid century furniture business. I'm participating in an antiques fair prior to the website launch. I'd like a 1 page flyer that highlights a sampling of some iconic pieces and invites people to check out the website soon. If possible, I'd also like a Word template for a tear sheet (a one page doc that has the company logo and contact info, a picture of the item, a field for description and dimensions). The following is an example of a tear sheet...http://www.qxbtimbercraft.example/uploads/2/2/7/5/2275376/zephon_oak_rail_side_seat.pdf. I'd prefer a smaller slot for the image (maybe one side of the page) and a much larger area for description and dimensions (as its vintage furniture I'll need to report on condition).

I've attached a few sample pieces of furniture, the company logo, contact information, and a room that included furniture from the business. The color palette for the business is orange, black, white and gray.

Target Market(s)

Potential Customers.....

Industry/Entity Type

Retail

Font styles to use
Other font styles liked:
• I think the fonts should be similar to the ones used in the logo and the business card (see attached)

Colors
f37122
1b1b1b
ebebeb

Requirements
Must have
• An elegant clean look and feel (although its a mid century furniture business I don't carry kitschy items...just really beautiful classic high-end pieces). It should highlight the beauty of the furniture and provide contact information.

```html
<!DOCTYPE html>
<html lang="en">
<head>
<meta charset="utf-8">
<title>Atelier Vireo Crandt – Flyer Samples</title>
<link href="https://fonts.googleapis.com/css2?family=Arimo:wght@400;700&display=swap" rel="stylesheet">
<style>
:root{
  --orange:#f37122;
  --ink:#1b1b1b;
  --light:#ebebeb;
  --board:#9c9c9c;
  --text:#2a2a2a;
  --panel:rgba(22,20,18,.9);
}
*{box-sizing:border-box;margin:0;padding:0}
html,body{width:1200px;height:829px;overflow:hidden}
body{background:var(--board);font-family:"Arimo",Arial,sans-serif;position:relative;color:var(--text)}
.flyer{position:absolute;top:72px;width:491px;height:637px;background:#fff;box-shadow:0 3px 10px rgba(0,0,0,.35);overflow:hidden}
.flyer--light{left:67px}
.flyer--dark{left:632px}
.caption{position:absolute;top:748px;width:491px;text-align:center;font-size:27px;color:#3a3a3a}
.caption--one{left:67px}.caption--two{left:632px}
.abs{position:absolute}
.wordmark{position:absolute;font-weight:400;white-space:nowrap;transform:translateX(-50%)}
.flyer--light .masthead{left:0;top:0;width:491px;height:60px;background:var(--light)}
.flyer--light .wordmark{left:245px;top:17px;font-size:22px;letter-spacing:1.5px;color:var(--ink)}
.photo{background:linear-gradient(135deg,#5a4736 0%,#8a7258 35%,#c2a47e 55%,#6b5440 80%,#3b2e24 100%)}
.frame{border:1px solid rgba(255,255,255,.9)}
.cabinet{background:linear-gradient(160deg,#6c5a48,#a8966a 45%,#8b7a52 70%,#5a4a3a)}
.chair{background:linear-gradient(160deg,#7a5c44,#c9b04a 50%,#8e7a3a)}
.sideboard{background:linear-gradient(160deg,#6a4f40,#2a211c 50%,#1b1714)}
.heading{position:absolute;font-size:15px;color:var(--ink);white-space:nowrap;padding-left:6px;border-left:1px solid #777;line-height:15px}
.heading b{color:var(--orange);font-weight:700}
.copy{position:absolute;width:211px;font-size:7.8px;line-height:9.6px;text-align:justify}
.copy p+p{margin-top:9px}
.dims{position:absolute;width:192px;border-collapse:collapse;font-size:7.6px}
.dims td{height:16px;padding:0 3px}
.dims td:last-child{text-align:right;padding-right:10px}
.flyer--light .dims tr:nth-child(odd){background:#e4e4e4}
.contact{position:absolute;left:26px;top:608px;font-size:8.2px;white-space:nowrap;color:var(--ink)}
.contact span{color:var(--orange)}
.contact i{font-style:normal;color:#777;margin:0 7px}
.bar{position:absolute;left:0;top:626px;width:491px;height:11px}
.flyer--dark .panel{left:237px;top:0;width:254px;height:490px;background:var(--panel)}
.flyer--dark .wordmark{left:364px;top:28px;font-size:15px;letter-spacing:1px;color:var(--orange)}
.flyer--dark .heading{color:#fff;border-left-color:#ccc}
.flyer--dark .copy{color:#e6e6e6}
.flyer--dark .dims{color:#e6e6e6}
.flyer--dark .dims tr{border-bottom:1px solid rgba(255,255,255,.45)}
.flyer--dark .dims tr:last-child{border-bottom:none}
</style>
</head>
<body>

<section class="flyer flyer--light">
  <div class="abs masthead"></div>
  <div class="wordmark">ATELIER VIREO CRANDT</div>
  <div class="abs photo" style="left:0;top:66px;width:491px;height:308px" role="img" aria-label="Interior photograph of a furnished living room with shelves, artwork and chairs"></div>
  <div class="abs frame" style="left:19px;top:86px;width:452px;height:276px"></div>
  <div class="abs cabinet" style="left:274px;top:316px;width:196px;height:121px" role="img" aria-label="Photograph of a brass-front chest of drawers against a brick wall"></div>

  <div class="heading" style="left:26px;top:396px"><b>PRODUCT</b> DESCRIPTION</div>
  <div class="copy" style="left:26px;top:420px">
    <p>Lorem Ipsum is simply dummy text of the printing and typesetting industry. Lorem Ipsum has been the industry's standard dummy text ever since the 1500s, when an unknown printer took a galley of type and scrambled it to make a type specimen book. It has survived not only five centuries, but also the leap into electronic typesetting, remaining essentially unchanged. It was popularised in the 1960s with the release of Letraset sheets containing Lorem Ipsum passages, and more recently with desktop publishing software like Aldus PageMaker including versions of Lorem Ipsum.</p>
    <p>Lorem Ipsum is simply dummy text of the printing and typesetting industry. Lorem Ipsum has been the industry's standard dummy text ever since the 1500s, when an unknown printer took a galley of type and scrambled it to make a type specimen book.</p>
  </div>

  <div class="heading" style="left:277px;top:461px"><b>PRODUCT</b> DIMENSIONS</div>
  <table class="dims" style="left:274px;top:485px">
    <tr><td>Lorem Ipsum is simply dummy text</td><td>0.00</td></tr>
    <tr><td>Lorem Ipsum is simply dummy text</td><td>0.00</td></tr>
    <tr><td>Lorem Ipsum is simply dummy text</td><td>0.00</td></tr>
    <tr><td>Lorem Ipsum is simply dummy text</td><td>0.00</td></tr>
    <tr><td>Lorem Ipsum is simply dummy text</td><td>0.00</td></tr>
  </table>

  <div class="contact"><span>O:</span> 555-014-2290<i>|</i><span>M:</span> 555-014-6176<i>|</i><span>E:</span> hello@ateliervireocrandt.example<i>|</i><span>W:</span> www.ateliervireocrandt.example</div>
  <svg class="bar" viewBox="0 0 491 11" preserveAspectRatio="none" aria-hidden="true">
    <polygon points="0,0 343,0 337,11 0,11" fill="#f37122"/>
    <polygon points="345,0 491,0 491,11 339,11" fill="#1b1b1b"/>
  </svg>
</section>

<section class="flyer flyer--dark">
  <div class="abs photo" style="left:0;top:0;width:491px;height:536px" role="img" aria-label="Interior photograph of a living room with a lattice-back armchair, bench and sideboard"></div>
  <div class="abs panel"></div>
  <div class="wordmark">ATELIER VIREO CRANDT</div>

  <div class="heading" style="left:258px;top:80px"><b>PRODUCT</b> DESCRIPTION</div>
  <div class="copy" style="left:258px;top:102px">
    <p>Lorem Ipsum is simply dummy text of the printing and typesetting industry. Lorem Ipsum has been the industry's standard dummy text ever since the 1500s, when an unknown printer took a galley of type and scrambled it to make a type specimen book. It has survived not only five centuries, but also the leap into electronic typesetting, remaining essentially unchanged. It was popularised in the 1960s with the release of Letraset sheets containing Lorem Ipsum passages, and more recently with desktop publishing software like Aldus PageMaker including versions of Lorem Ipsum.</p>
    <p>Lorem Ipsum is simply dummy text of the printing and typesetting industry. Lorem Ipsum has been the industry's standard dummy text ever since the 1500s, when an unknown printer took a galley of type and scrambled it to make a type specimen book.</p>
  </div>

  <div class="heading" style="left:260px;top:297px"><b>PRODUCT</b> DIMENSIONS</div>
  <table class="dims" style="left:258px;top:319px">
    <tr><td>Lorem Ipsum is simply dummy text</td><td>0.00</td></tr>
    <tr><td>Lorem Ipsum is simply dummy text</td><td>0.00</td></tr>
    <tr><td>Lorem Ipsum is simply dummy text</td><td>0.00</td></tr>
    <tr><td>Lorem Ipsum is simply dummy text</td><td>0.00</td></tr>
    <tr><td>Lorem Ipsum is simply dummy text</td><td>0.00</td></tr>
  </table>

  <div class="abs cabinet" style="left:26px;top:490px;width:143px;height:100px" role="img" aria-label="Photograph of a brass-front chest of drawers"></div>
  <div class="abs chair" style="left:177px;top:490px;width:143px;height:100px" role="img" aria-label="Photograph of a yellow upholstered lounge chair"></div>
  <div class="abs sideboard" style="left:327px;top:490px;width:143px;height:100px" role="img" aria-label="Photograph of a dark lacquered sideboard with brass pulls"></div>

  <div class="contact"><span>O:</span> 555-014-2290<i>|</i><span>M:</span> 555-014-6176<i>|</i><span>E:</span> hello@ateliervireocrandt.example<i>|</i><span>W:</span> www.ateliervireocrandt.example</div>
  <svg class="bar" viewBox="0 0 491 11" preserveAspectRatio="none" aria-hidden="true">
    <polygon points="0,0 343,0 337,11 0,11" fill="#f37122"/>
    <polygon points="345,0 491,0 491,11 339,11" fill="#1b1b1b"/>
  </svg>
</section>

<div class="caption caption--one">FLyer Sample_1</div>
<div class="caption caption--two">FLyer Sample_2</div>

</body>
</html>
```